SUPPLEMENT BOTTLE LABEL: DRUMMOND

We need a NEW FRESH look to her labels. Something contemporary, clean and professional. The colors need to remain the same but everything else can change, even the logo.

THE CURRENT LABEL IS ATTACHED IN PDF FORMAT

Target Market(s)

WOMEN BETWEEN 35-60

Requirements
Must have
• SAME COLORS
• FRESH
• CLEAN

```html
<!DOCTYPE html>
<html lang="en">
<head>
<meta charset="utf-8">
<title>Balanced Renew Cleanse Label</title>
<link href="https://fonts.googleapis.com/css2?family=Marcellus&family=Tinos:wght@400;700&display=swap" rel="stylesheet">
<style>
  :root {
    --page-bg: #f6f5f3;
    --label-top: #f8faf6;
    --label-bottom: #e3f1da;
    --ink: #1c1c1c;
    --cocoa: #9a4a22;
    --cocoa-soft: #a5643f;
  }
  * { margin: 0; padding: 0; box-sizing: border-box; }
  html, body {
    width: 1200px;
    height: 985px;
    overflow: hidden;
    background: var(--page-bg);
  }
  .label {
    position: absolute;
    left: 140px;
    top: 67px;
    width: 920px;
    height: 850px;
    background: linear-gradient(to bottom, var(--label-top) 0%, var(--label-top) 25%, var(--label-bottom) 100%);
    color: var(--ink);
    text-align: center;
    font-family: "Tinos", "Times New Roman", serif;
  }
  .label > * { position: absolute; left: 0; right: 0; }
  .brand {
    top: 100px;
    font-family: "Marcellus", serif;
    font-size: 52px;
    letter-spacing: 2px;
  }
  .product {
    top: 275px;
    font-family: "Marcellus", serif;
    font-size: 122px;
    line-height: 1;
    letter-spacing: 1px;
  }
  .flavor {
    top: 410px;
    font-size: 38px;
    font-weight: 700;
    letter-spacing: 11px;
    color: var(--cocoa);
  }
  .flavor-rule {
    top: 461px;
    left: 290px;
    right: 290px;
    height: 2px;
    background: var(--cocoa);
  }
  .flavor-note {
    top: 465px;
    font-size: 26px;
    color: var(--cocoa-soft);
  }
  .description {
    top: 578px;
    font-size: 29px;
    line-height: 35px;
  }
  .notice {
    top: 666px;
    font-size: 27px;
    line-height: 37px;
  }
  .net-rule {
    top: 745px;
    left: 205px;
    right: 205px;
    height: 2px;
    background: var(--ink);
  }
  .net-weight {
    top: 756px;
    font-size: 37px;
    font-weight: 700;
  }
</style>
</head>
<body>
  <main class="label">
    <div class="brand">BALANCED RENEW</div>
    <h1 class="product">CLEANSE</h1>
    <div class="flavor">Chocolate</div>
    <div class="flavor-rule"></div>
    <div class="flavor-note">with other natural flavors</div>
    <p class="description">Collagen, Multivitamin, Mineral &amp;<br>Herbal Dietary Supplement Powder</p>
    <p class="notice">Notice: Use this product as a food supplement only.<br>Do not use for weight reduction.</p>
    <div class="net-rule"></div>
    <div class="net-weight">NET WT. 1.21 LBS (551.2 G)</div>
  </main>
</body>
</html>
```